Marigold comb home studio

MARIGOLD COMB.....at fox valley ,Wahroonga is a home hairdressing studio.
Hair services from a peaceful setting.
Quality colours and products.
free consultation prior to making appointment.
Easy and convenient after hours hair appointments.
Qualified hairdresser with over 15 years experience.
Specialise in foiling,balayage,ombre colour,tints,style cutting and blowdrying.
20 % off for new clients(colour services)
sms or call for 0493620174 for a quote.
Updates
im sorry guys but i has to re do alot of the photos. i would like something that looks elegant and classy.i will post an example of a flier style i like Added Wednesday, April 27, 2016
Project Deadline Extended Reason: im sorry i have decided i needed better photographs. please design again...i will choose someone before the deadline. please an elegant design will be great Added Wednesday, April 27, 2016
Target Market(s)
18-60 year olds
Industry/Entity Type
Hair
Requirements
Must have
- Must say home hairdressing studio
- Must say Marigold Comb at Willow Vale Ashgrove
- Must say phone number
Nice to have
- Modern but still classy and elegant
- Try to incorporate any photos which I have uploaded that looks best

```html
<!DOCTYPE html>
<html lang="en">
<head>
<meta charset="utf-8">
<title>Marigold Comb – Home Hairdressing Studio Flyer</title>
<link href="https://fonts.googleapis.com/css2?family=Raleway:wght@300;400;600;700;800&display=swap" rel="stylesheet">
<style>
  :root {
    --page: #e9e6e2;
    --ink: #050407;
    --white: #ffffff;
    --soft-white: #e8e6ea;
    --pink: #e0318f;
    --purple: #5b2a9c;
    --purple-deep: #2e0f5c;
    --violet: #8a4fd1;
    --hair-dark: #3a2a20;
    --hair-warm: #8c6a4e;
    --skin: #d9b8a6;
    --room: #cfc7bd;
    --room-dark: #7a6e64;
  }
  * { box-sizing: border-box; margin: 0; padding: 0; }
  html, body { width: 1200px; height: 684px; overflow: hidden; background: var(--page); }
  body { font-family: "Raleway", "Helvetica Neue", Arial, sans-serif; color: var(--white); }

  .flyer {
    position: absolute; left: 142px; top: 22px;
    width: 915px; height: 640px;
    background: var(--ink); overflow: hidden;
    box-shadow: 0 8px 24px rgba(0,0,0,.25);
  }

  .hero-photo {
    position: absolute; left: 400px; top: 0; width: 515px; height: 640px;
    background:
      radial-gradient(ellipse 40% 35% at 68% 42%, var(--skin) 0%, rgba(217,184,166,.6) 45%, transparent 75%),
      linear-gradient(100deg, var(--ink) 0%, var(--hair-dark) 22%, var(--hair-warm) 55%, var(--hair-dark) 85%, #2a1e18 100%);
  }
  .hero-photo::before {
    content: ""; position: absolute; inset: 0;
    background: linear-gradient(90deg, var(--ink) 0%, rgba(5,4,7,.6) 18%, transparent 45%);
  }

  .bands { position: absolute; inset: 0; pointer-events: none; }

  .title {
    position: absolute; left: 147px; top: 30px;
    font-weight: 300; font-size: 52px; letter-spacing: 1px; line-height: 1;
  }
  .location {
    position: absolute; left: 70px; top: 94px;
    font-weight: 600; font-size: 22px; color: var(--pink); line-height: 1;
    white-space: nowrap;
  }
  .offer {
    position: absolute; left: 106px; top: 133px;
    font-size: 20px; font-weight: 400; line-height: 1;
  }
  .offer strong { font-size: 31px; font-weight: 800; letter-spacing: .5px; }

  .contact { position: absolute; right: 50px; top: 38px; text-align: left; }
  .contact-call { font-size: 13.5px; font-weight: 400; letter-spacing: .3px; }
  .contact-phone { font-size: 30px; font-weight: 400; letter-spacing: 1px; line-height: 1.05; }

  .specialties {
    position: absolute; left: 52px; top: 194px;
    font-size: 13px; line-height: 18.5px; text-transform: uppercase;
  }
  .specialties h2 { font-size: 13px; font-weight: 700; }
  .specialties ul { list-style: none; font-weight: 400; }
  .specialties li::before { content: "* "; margin-right: 4px; }

  .quality {
    position: absolute; left: 256px; top: 194px;
    list-style: none; font-size: 13px; font-weight: 700; line-height: 18.5px;
    text-transform: uppercase;
  }
  .quality li::before { content: "• "; }

  .tile { position: absolute; top: 354px; width: 185px; }
  .tile-photo { height: 129px; border: 2px solid var(--soft-white); }
  .tile-photo.room { background: linear-gradient(180deg, #efeae4 0%, var(--room) 60%, var(--room-dark) 100%); }
  .tile-photo.portrait { background: radial-gradient(ellipse 35% 45% at 50% 45%, var(--skin), var(--hair-warm) 65%, var(--hair-dark) 100%); }
  .tile-label {
    height: 34px; background: var(--ink); text-align: center;
    font-size: 22px; line-height: 34px; text-transform: uppercase;
  }
  .tile-label.bold { font-weight: 800; }
  .tile-label.light { font-weight: 300; }
  .tile-label .accent { color: var(--pink); font-size: 16px; }
  .tile-style { left: 39px; }
  .tile-beauty { left: 243px; }
  .tile-comfort { left: 446px; }

  .divider { position: absolute; left: 55px; top: 536px; width: 579px; height: 1px; background: var(--soft-white); }
  .divider::after {
    content: ""; position: absolute; left: 273px; top: -4px;
    width: 9px; height: 9px; border-radius: 50%; background: var(--white);
  }

  .perk {
    position: absolute; top: 551px;
    font-size: 14px; font-weight: 700; line-height: 18px; text-transform: uppercase;
  }
  .perk-consult { left: 55px; }
  .perk-hours { left: 367px; }
</style>
</head>
<body>
  <main class="flyer">
    <div class="hero-photo" role="img" aria-label="Portrait of a woman with long glossy brown hair and pink lips"></div>

    <svg class="bands" width="915" height="640" viewBox="0 0 915 640" aria-hidden="true">
      <defs>
        <linearGradient id="band-top" x1="0" y1="0" x2="1" y2="0">
          <stop offset="0" stop-color="#5b2a9c" stop-opacity="0"/>
          <stop offset=".4" stop-color="#5b2a9c"/>
          <stop offset="1" stop-color="#8a4fd1"/>
        </linearGradient>
        <linearGradient id="band-bottom" x1="0" y1="0" x2="1" y2="0">
          <stop offset="0" stop-color="#5b2a9c"/>
          <stop offset=".6" stop-color="#2e0f5c"/>
          <stop offset="1" stop-color="#2e0f5c" stop-opacity="0"/>
        </linearGradient>
      </defs>
      <path d="M420 0 L915 0 L915 20 Q700 6 420 0 Z" fill="url(#band-top)"/>
      <path d="M0 570 Q300 620 720 640 L0 640 Z" fill="url(#band-bottom)"/>
      <path d="M0 600 Q280 628 560 640 L0 640 Z" fill="#8a4fd1" opacity=".55"/>
    </svg>

    <h1 class="title">MARIGOLD COMB</h1>
    <p class="location">at Willow Vale Ashgrove home hairdressing studio</p>
    <p class="offer"><strong>20% OFF</strong> FOR NEW CLIENTS(COLOUR SERVICES)</p>

    <div class="contact">
      <p class="contact-call">CALL DELPHINE FOR A QUOTE</p>
      <p class="contact-phone">049-362-0174</p>
    </div>

    <section class="specialties">
      <h2>Specialties</h2>
      <ul>
        <li>Foiling</li>
        <li>Balayage</li>
        <li>Ombre colour</li>
        <li>Tints</li>
        <li>Style cutting</li>
        <li>Blowdrying</li>
      </ul>
    </section>
    <ul class="quality">
      <li>Quality colours</li>
      <li>Quality products</li>
      <li>Over 15 years experience</li>
    </ul>

    <figure class="tile tile-style">
      <div class="tile-photo room" role="img" aria-label="Bright salon room with mirror and console table"></div>
      <figcaption class="tile-label bold">Style</figcaption>
    </figure>
    <figure class="tile tile-beauty">
      <div class="tile-photo portrait" role="img" aria-label="Woman with voluminous curled brown hair"></div>
      <figcaption class="tile-label light">Beautiful <span class="accent">you</span></figcaption>
    </figure>
    <figure class="tile tile-comfort">
      <div class="tile-photo room" role="img" aria-label="Salon styling chair in front of a tall mirror"></div>
      <figcaption class="tile-label bold">Comfort</figcaption>
    </figure>

    <div class="divider"></div>
    <p class="perk perk-consult">Free consultation prior to<br>making appointment</p>
    <p class="perk perk-hours">Easy and convenient after<br>hours hair appointments</p>
  </main>
</body>
</html>
```